Complete Stationary Package for IT Company
Full Stationary (Folder, Envolope, etc) + CD Cover + Background for PC
Complete Stationary Package for IT Company - Information Technology
Marco Vellida
Gerente General
C/Ramon Ferrel #27, Lomas de Vistral, Santo Domingo Este. RD.
marcovellida@qnv.com.do
www.qnv.com.do
marcovellida marcovellida
Hi! Nice work! Could put a QR Code with Contact full Info?
Hi! Please include this text: Aplicaciones * Consultoria * Infraestructura * Soporte

```html
<!DOCTYPE html>
<html lang="es">
<head>
<meta charset="utf-8">
<title>QNV Dominicana – Tarjetas de presentación</title>
<link href="https://fonts.googleapis.com/css2?family=Montserrat:wght@500;700&display=swap" rel="stylesheet">
<style>
  :root {
    --slate: #4f7183;
    --orange: #f39a2b;
    --paper: #ffffff;
    --backdrop: #d9dadb;
    --ink-soft: #6d7378;
  }
  * { margin: 0; padding: 0; box-sizing: border-box; }
  html, body { width: 1200px; height: 987px; overflow: hidden; }
  body {
    background: var(--backdrop);
    font-family: "Montserrat", Arial, sans-serif;
    position: relative;
  }
  .card {
    position: absolute;
    left: 250px;
    width: 700px;
    height: 400px;
    border-radius: 22px;
    background: var(--paper);
    overflow: hidden;
  }
  .card--front { top: 60px; }
  .card--back { top: 520px; }

  .brand-name {
    position: absolute;
    color: var(--slate);
    font-weight: 700;
    line-height: 1;
    white-space: nowrap;
  }
  .card--front .brand-name {
    left: 0; right: 0; top: 150px;
    text-align: center;
    font-size: 44px;
    letter-spacing: 1px;
  }
  .tagline {
    position: absolute; left: 0; right: 0; top: 258px;
    text-align: center;
    font-size: 10px; font-weight: 500;
    letter-spacing: 3px; text-transform: uppercase;
    color: var(--ink-soft);
  }

  .card__shape { position: absolute; inset: 0; }
  .card--back .brand-name {
    left: 200px; right: 40px; top: 60px;
    text-align: center;
    font-size: 52px;
    letter-spacing: 1px;
  }

  .holder { position: absolute; left: 42px; top: 270px; color: var(--paper); text-transform: uppercase; font-weight: 500; }
  .holder__name { font-size: 17px; letter-spacing: 3px; }
  .holder__role { font-size: 12px; letter-spacing: 3px; margin-top: 8px; }

  .contact { position: absolute; left: 420px; top: 262px; list-style: none; color: var(--paper); font-size: 10px; font-weight: 500; letter-spacing: 0.8px; }
  .contact li { display: flex; align-items: center; gap: 7px; height: 17px; white-space: nowrap; }
  .contact li.contact__cont { padding-left: 19px; }
  .contact svg { width: 12px; height: 12px; flex: none; }
</style>
</head>
<body>

  <section class="card card--front" aria-label="Tarjeta, anverso">
    <p class="brand-name">QNV Dominicana</p>
    <p class="tagline">Aplicaciones | Consultoria | Infraestructura | Soporte</p>
  </section>

  <section class="card card--back" aria-label="Tarjeta, reverso">
    <svg class="card__shape" viewBox="0 0 700 400" preserveAspectRatio="none">
      <path d="M0,205 Q360,300 700,170 L700,400 L0,400 Z" fill="var(--slate)"/>
      <path d="M0,168 Q360,290 700,138" fill="none" stroke="var(--orange)" stroke-width="12"/>
    </svg>

    <p class="brand-name">QNV Dominicana</p>

    <div class="holder">
      <p class="holder__name">Marco Vellida</p>
      <p class="holder__role">Gerente General</p>
    </div>

    <ul class="contact">
      <li>
        <svg viewBox="0 0 12 12"><circle cx="6" cy="6" r="6" fill="#fff"/><path d="M6 2.5a2 2 0 0 0-2 2c0 1.6 2 4.5 2 4.5s2-2.9 2-4.5a2 2 0 0 0-2-2z" fill="var(--slate)"/></svg>
        C/Ramon Ferrel #27, Lomas
      </li>
      <li class="contact__cont">de Vistral, Santo Domingo Este. RD.</li>
      <li>
        <svg viewBox="0 0 12 12"><circle cx="6" cy="6" r="6" fill="#fff"/><rect x="4.3" y="2.6" width="3.4" height="6.8" rx="0.8" fill="var(--slate)"/></svg>
        809.555.0142
      </li>
      <li>
        <svg viewBox="0 0 12 12"><circle cx="6" cy="6" r="6" fill="#fff"/><path d="M3.5 3.2l1.6-.3.8 1.8-1 .8a5 5 0 0 0 1.8 1.8l.8-1 1.8.8-.3 1.6C6 8.8 3.2 6 3.5 3.2z" fill="var(--slate)"/></svg>
        829.555.0178
      </li>
      <li>
        <svg viewBox="0 0 12 12"><circle cx="6" cy="6" r="6" fill="#fff"/><rect x="2.8" y="3.8" width="6.4" height="4.4" fill="var(--slate)"/><path d="M2.8 3.8L6 6.3l3.2-2.5" fill="none" stroke="#fff" stroke-width="0.7"/></svg>
        marcovellida@qnv.com.do
      </li>
      <li>
        <svg viewBox="0 0 12 12"><circle cx="6" cy="6" r="6" fill="#fff"/><circle cx="6" cy="6" r="3.2" fill="none" stroke="var(--slate)" stroke-width="0.8"/><path d="M2.8 6h6.4M6 2.8c-1.5 1.8-1.5 4.6 0 6.4M6 2.8c1.5 1.8 1.5 4.6 0 6.4" fill="none" stroke="var(--slate)" stroke-width="0.7"/></svg>
        www.qnv.com.do
      </li>
    </ul>
  </section>

</body>
</html>
```